Word template Letterhead for Australian Law Firm

We are a small law firm based in Manly, NSW, Australia. We have had a new logo designed for us and wish to freshen up the appearance of our letterhead. We require the letterhead to be in a word document that we can type over. This will not be a ‘printed’ letterhead because we send the majority of our correspondence via email. We would like to see a few options. We have attached our previous letterhead as well as the artwork for our new logo. We like the idea of a watermark across the bottom of the letter but the watermark must stay in place and we must be able to type over it. We are open to some colour throughout the letterhead because the majority of our correspondence is sent electronically. We also use electronic signatures. I have uploaded an example of this.The letterhead must include:-1. Our address details – including our phone number, physical address, website address etc. These details can be found on the copy of our previous letterhead;2. ABN Number;3. The words ‘Brevicor (NSW) Pty Ltd ACN 482 731 058 trading as Shipton & AssociatesLiability limited by a scheme approved under Professional Standards Legislation. The letterhead does not need to include the names and qualifications of the people working at the firm. Thank you.

Target Market(s)

Clients and other parties

Industry/Entity Type

Law Firm

Font styles to use
Other font styles liked:
• raleway, montserrat

Colors

Designer to choose colors to be used in the design.

Requirements
Must have
• Certain wording - please see project description.
• Must be a word document and must be able to type over the watermark etc.
Nice to have
• Watermark at the bottom of the letter.

```html
<!DOCTYPE html>
<html lang="en">
<head>
<meta charset="utf-8">
<title>Kervell &amp; Associates — Letterhead</title>
<link rel="stylesheet" href="https://fonts.googleapis.com/css2?family=Montserrat:wght@400;500;700;800&family=Passion+One:wght@700&display=swap">
<style>
  :root {
    --maroon: #551b34;
    --ink: #111111;
    --white: #ffffff;
    --watermark-grey: #d2d2d2;
    --badge-grey: #e4e4e6;
    --page: #ffffff;
  }
  html, body {
    margin: 0;
    padding: 0;
    width: 848px;
    height: 1200px;
    overflow: hidden;
    background: var(--page);
  }
  .letterhead {
    position: relative;
    width: 848px;
    height: 1200px;
    font-family: "Montserrat", sans-serif;
    color: var(--ink);
  }
  .role-tab {
    position: absolute;
    left: 52px;
    top: 52px;
    width: 202px;
    height: 51px;
  }
  .role-tab svg { position: absolute; inset: 0; }
  .role-tab__label {
    position: absolute;
    left: 15px;
    top: 5px;
    font-weight: 700;
    font-size: 34px;
    line-height: 40px;
    color: var(--white);
  }
  .staff-list {
    position: absolute;
    left: 52px;
    top: 112px;
    margin: 0;
    font-size: 13px;
    line-height: 15.6px;
    display: grid;
    grid-template-columns: 116px 11px auto;
  }
  .staff-list dt, .staff-list dd { margin: 0; white-space: nowrap; }
  .staff-list .name { font-weight: 800; }
  .staff-list .quals { font-size: 11.5px; }
  .firm-name {
    position: absolute;
    right: 40px;
    top: 42px;
    margin: 0;
    font-family: "Passion One", sans-serif;
    font-weight: 700;
    font-size: 40px;
    line-height: 48px;
    letter-spacing: 0.2px;
    color: var(--ink);
  }
  .contact {
    position: absolute;
    right: 40px;
    top: 95px;
    text-align: right;
    font-size: 13px;
    line-height: 15.6px;
    font-style: normal;
  }
  .contact p { margin: 0 0 15.6px; }
  .watermark-name {
    position: absolute;
    left: 0;
    width: 848px;
    top: 540px;
    text-align: center;
    font-weight: 400;
    font-size: 30px;
    line-height: 36px;
    color: var(--watermark-grey);
  }
  .accreditation-badge {
    position: absolute;
    left: 329px;
    top: 686px;
    width: 210px;
    height: 210px;
  }
  .footer-band {
    position: absolute;
    left: 52px;
    top: 1102px;
    width: 756px;
    height: 62px;
  }
  .footer-band svg { position: absolute; inset: 0; }
  .footer-band__text {
    position: absolute;
    left: 7px;
    top: 9px;
    font-size: 13px;
    line-height: 15.6px;
    color: var(--white);
    margin: 0;
    white-space: nowrap;
  }
</style>
</head>
<body>
<main class="letterhead">
  <div class="role-tab">
    <svg width="202" height="51" viewBox="0 0 202 51" aria-hidden="true">
      <path d="M0 0 H173 C179 0 183 3 185 8 L202 51 H0 Z" fill="var(--maroon)"/>
    </svg>
    <span class="role-tab__label">Solicitors</span>
  </div>

  <dl class="staff-list">
    <dt>Principal IPL</dt><dd>:</dd><dd><span class="name">R. HALLORAN</span>, Dip Law, Acc Spec (Fam)</dd>
    <dt>Consultant</dt><dd>:</dd><dd><span class="name">P. D. KERVELL</span><span class="quals">, BEc, LLB, Acc Spec (Fam)</span></dd>
    <dt>Senior Associate</dt><dd>:</dd><dd><span class="name">T. A. BRENNAN</span><span class="quals">, LLB</span></dd>
    <dt>Associate</dt><dd>:</dd><dd><span class="name">L. OKAFOR</span><span class="quals">, BSc MEthics JD</span></dd>
  </dl>

  <h1 class="firm-name">Kervell &amp; Associates</h1>

  <address class="contact">
    <p>SUITE 4, 22 CORSO LANE<br>HARBOURVALE NSW 2099</p>
    <p>TELEPHONE: (02) 9000 4181<br>FACSIMILE: (02) 9000 4182</p>
    <p>Email: reception@brevicorlaw.com.au<br>ABN: 84 482 731 058<br>www.kervellandassociates.com.au</p>
  </address>

  <div class="watermark-name">Kervell &amp; Associates</div>

  <svg class="accreditation-badge" viewBox="0 0 210 210" role="img" aria-label="Accreditation badge">
    <circle cx="105" cy="105" r="92" fill="none" stroke="var(--badge-grey)" stroke-width="14"/>
  </svg>

  <footer class="footer-band">
    <svg width="756" height="62" viewBox="0 0 756 62" aria-hidden="true">
      <path d="M0 0 H642 C670 0 689 8 704 19 L756 62 H0 Z" fill="var(--maroon)"/>
    </svg>
    <p class="footer-band__text">Brevicor (NSW) Pty Ltd ACN 482 731 058 trading as Kervell &amp; Associates<br>Liability limited by a scheme approved under Professional Standards Legislation. Legal practitioners at<br>Brevicor (NSW) Pty Ltd are members of the scheme.</p>
  </footer>
</main>
</body>
</html>
```